Marketing Collateral for Construction Company
Keystone Cellar Craftworks
Attention Designers:
I have uploaded a number of pictures of basement project that our company has done. Please use these pictures where you think they will work in the designs for the marketing peripherals.
Thank you,
Mark
where is the content for the flyer and brochure?
@QW - please check your private messages on top right corner once you login to your account & reply. Thanks
Designers,
I have changed the scope of the project only to include:
-tri-fold brochure
-flyer
-door hanger
I have also uploaded AI files for you to use in your designs. Please let me know if you need more source files or a different format.
Thanks,

```html
<!DOCTYPE html>
<html lang="en">
<head>
<meta charset="utf-8">
<title>Keystone Cellar Craftworks – Collateral</title>
<link rel="stylesheet" href="https://fonts.googleapis.com/css2?family=PT+Serif:wght@400;700&display=swap">
<style>
  :root{
    --bg:#e7e4df;
    --blue:#1b63ad;
    --blue-dark:#0c3f7c;
    --blue-light:#3a8fd6;
    --green:#4b9a2c;
    --green-light:#86c440;
    --ink:#1f2d3d;
    --paper:#ffffff;
  }
  *{box-sizing:border-box;margin:0;padding:0}
  html,body{width:1200px;height:847px;overflow:hidden;background:var(--bg)}
  body{position:relative;font-family:"PT Serif",Georgia,serif;color:var(--ink)}
  .piece{position:absolute;box-shadow:0 4px 14px rgba(0,0,0,.25);background:var(--paper);overflow:hidden}
  .piece svg.bg{position:absolute;inset:0;width:100%;height:100%}
  .txt{position:absolute;font-size:6.5px;line-height:1.45}
  .light{color:#fff}
  h2{font-weight:700;font-size:13px;margin-bottom:6px}
  .brand{position:absolute;display:flex;align-items:center;gap:5px;font-weight:700;color:var(--blue-dark);line-height:1.05}
  .brand .dot{width:12px;height:12px;border-radius:50%;background:var(--green);flex:none}
  .tagline{position:absolute;font-size:6px;color:var(--blue-dark)}
  ul{list-style:none}
  .service-list{text-align:right;white-space:nowrap}

  .brochure-outside{left:163px;top:108px;width:473px;height:305px}
  .flyer{left:679px;top:77px;width:310px;height:456px;box-shadow:none}
  .brochure-inside{left:163px;top:468px;width:473px;height:324px}
  .hanger{position:absolute;top:540px;width:146px;height:259px}
  .hanger-blue{left:674px}
  .hanger-green{left:836px}
</style>
</head>
<body>

<!-- Tri-fold brochure, outside -->
<section class="piece brochure-outside">
  <svg class="bg" viewBox="0 0 473 305" preserveAspectRatio="none">
    <defs>
      <linearGradient id="boBlue" x1="0" y1="0" x2="1" y2="1">
        <stop offset="0" stop-color="#0c3f7c"/><stop offset="1" stop-color="#3a8fd6"/>
      </linearGradient>
      <linearGradient id="boGreen" x1="0" y1="0" x2="1" y2="0">
        <stop offset="0" stop-color="#3d8a22"/><stop offset="1" stop-color="#86c440"/>
      </linearGradient>
    </defs>
    <path d="M0 0H315C235 60 215 190 250 305H0Z" fill="url(#boBlue)"/>
    <path d="M315 0C245 60 228 185 262 305" fill="none" stroke="#fff" stroke-width="6"/>
    <path d="M200 305C270 240 370 222 473 214V305Z" fill="url(#boGreen)"/>
    <path d="M190 305C265 232 370 210 473 204" fill="none" stroke="#fff" stroke-width="3"/>
    <line x1="158" y1="0" x2="158" y2="305" stroke="rgba(255,255,255,.15)"/>
    <line x1="315" y1="0" x2="315" y2="305" stroke="rgba(0,0,0,.06)"/>
  </svg>
  <div class="txt light" style="left:12px;top:14px;width:132px">
    <h2>Interior Design</h2>
    <p>Every space below your home holds quiet promise. Our crews turn raw concrete rooms into warm, bright living areas built around the way your family lives. From the first sketch to the final trim, we plan each detail with care, keep you informed at every step, and finish on schedule with lasting materials you can trust.</p>
  </div>
  <ul class="txt light service-list" style="left:166px;top:165px;width:58px;font-size:6px">
    <li>Basement Design</li><li>Interior Design</li><li>Basement Additions</li><li>Outdoor Spaces</li>
  </ul>
  <div class="txt light" style="left:330px;top:240px;font-size:6px">
    <p>Phone: 555-014-2290</p><p>Fax: 555-014-2291</p><p>info@keystonecellar.example</p><p>www.keystonecellar.example</p>
  </div>
  <div class="brand" style="left:335px;top:68px;font-size:13px;width:130px"><span class="dot"></span><span>Keystone Cellar Craftworks</span></div>
  <p class="tagline" style="left:352px;top:104px">Finished Basement Specialists</p>
</section>

<!-- Flyer -->
<section class="piece flyer">
  <svg class="bg" viewBox="0 0 310 456" preserveAspectRatio="none">
    <defs>
      <linearGradient id="flBlue" x1="0" y1="0" x2="1" y2="1">
        <stop offset="0" stop-color="#0c3f7c"/><stop offset="1" stop-color="#3a8fd6"/>
      </linearGradient>
      <linearGradient id="flGreen" x1="0" y1="0" x2="1" y2="0">
        <stop offset="0" stop-color="#3d8a22"/><stop offset="1" stop-color="#86c440"/>
      </linearGradient>
    </defs>
    <rect width="310" height="456" fill="#fff"/>
    <path d="M0 0H60C25 70 20 150 55 250C20 200 0 160 0 120Z" fill="url(#flBlue)"/>
    <path d="M0 320C90 300 200 290 310 300V456H0Z" fill="url(#flGreen)"/>
    <path d="M0 312C90 292 200 282 310 292" fill="none" stroke="var(--blue)" stroke-width="4"/>
  </svg>
  <div class="brand" style="left:150px;top:40px;font-size:15px;width:150px"><span class="dot"></span><span>Keystone Cellar Craftworks</span></div>
  <p class="tagline" style="left:170px;top:90px">Finished Basement Specialists</p>
  <p class="txt" style="left:90px;top:160px;width:200px;font-size:6.5px">We design and build finished basements, additions and custom interiors for homeowners across the region. Every project starts with listening, moves through honest planning, and ends with a space that feels like it was always part of your home.</p>
  <div class="txt light" style="left:22px;top:360px;font-size:6px">
    <p>Phone: 555-014-2290</p><p>Fax: 555-014-2291</p><p>info@keystonecellar.example</p><p>www.keystonecellar.example</p>
  </div>
  <p class="txt light" style="left:165px;top:360px;width:125px;font-size:6.5px">Call today for a free on-site consultation and design estimate.</p>
</section>

<!-- Tri-fold brochure, inside -->
<section class="piece brochure-inside">
  <svg class="bg" viewBox="0 0 473 324" preserveAspectRatio="none">
    <defs>
      <linearGradient id="biBlue" x1="0" y1="0" x2="1" y2="1">
        <stop offset="0" stop-color="#0c3f7c"/><stop offset="1" stop-color="#3a8fd6"/>
      </linearGradient>
      <linearGradient id="biGreen" x1="0" y1="0" x2="1" y2="1">
        <stop offset="0" stop-color="#3d8a22"/><stop offset="1" stop-color="#86c440"/>
      </linearGradient>
    </defs>
    <rect width="158" height="324" fill="url(#biBlue)"/>
    <path d="M158 0H200C170 100 175 220 205 324H158Z" fill="url(#biBlue)"/>
    <path d="M315 0H473V324H315C292 220 292 100 315 0Z" fill="url(#biGreen)"/>
    <path d="M315 0C292 100 292 220 315 324" fill="none" stroke="#fff" stroke-width="4"/>
    <path d="M200 0C170 100 175 220 205 324" fill="none" stroke="#fff" stroke-width="4"/>
  </svg>
  <div class="txt light" style="left:12px;top:14px;width:134px">
    <h2>About us</h2>
    <p>Founded by local builders, we have spent years finishing basements that families actually use. Our team handles framing, electrical, plumbing, drywall and finish carpentry in house, so one crew owns your project from start to finish. We treat every home as if it were our own and stand behind the work long after we leave.</p>
  </div>
  <div class="txt" style="left:200px;top:120px;width:86px">
    <h2 style="color:var(--blue-dark);font-size:12px">Special Design</h2>
    <p>Home theaters, guest suites, wet bars and playrooms shaped around your plans and budget.</p>
  </div>
  <div class="brand" style="left:204px;top:230px;font-size:9px;width:84px"><span class="dot"></span><span>Keystone Cellar Craftworks</span></div>
  <div class="txt light" style="left:326px;top:14px;width:136px">
    <h2>Basement Additions</h2>
    <p>Need more room without moving? We dig, pour and waterproof new lower levels that blend with your existing foundation, adding real square footage and value to your property for years to come.</p>
  </div>
</section>

<!-- Door hanger, blue -->
<section class="hanger hanger-blue">
  <svg class="bg" viewBox="0 0 146 259" width="146" height="259">
    <path d="M18 0H128Q146 0 146 18V259H0V18Q0 0 18 0Z" fill="var(--blue)"/>
    <path d="M0 110C50 90 100 95 146 110V200C100 185 50 185 0 200Z" fill="#fff"/>
    <circle cx="73" cy="42" r="22" fill="var(--bg)"/>
    <rect x="71" y="0" width="4" height="22" fill="var(--bg)"/>
  </svg>
  <div class="brand" style="left:14px;top:128px;font-size:11px;width:122px"><span class="dot"></span><span>Keystone Cellar Craftworks</span></div>
  <ul class="txt light" style="left:14px;top:208px;font-size:6px">
    <li>Basement Design</li><li>Interior Design</li><li>Basement Additions</li><li>Outdoor Spaces</li>
  </ul>
</section>

<!-- Door hanger, green -->
<section class="hanger hanger-green">
  <svg class="bg" viewBox="0 0 146 259" width="146" height="259">
    <path d="M18 0H128Q146 0 146 18V259H0V18Q0 0 18 0Z" fill="var(--green)"/>
    <path d="M0 110C50 90 100 95 146 110V200C100 185 50 185 0 200Z" fill="#fff"/>
    <circle cx="73" cy="42" r="22" fill="var(--bg)"/>
    <rect x="71" y="0" width="4" height="22" fill="var(--bg)"/>
  </svg>
  <div class="brand" style="left:14px;top:128px;font-size:11px;width:122px"><span class="dot"></span><span>Keystone Cellar Craftworks</span></div>
  <ul class="txt light" style="left:14px;top:208px;font-size:6px">
    <li>Basement Design</li><li>Interior Design</li><li>Basement Additions</li><li>Outdoor Spaces</li>
  </ul>
</section>

</body>
</html>
```